Father's 70th Birthday Poster/Canvas Word Art Creation

Looking for a word-art image in the shape of the station wagon image attached for a 70th birthday gift for our father. In other words, looking for the 70 phrases below to be organized in a way that you can see the Kestra station wagon outline. It can just be a simple outline of the wagon. I have also included an example of a Black Cab and another car Word Art for inspiration. Please notice how the words create the shape of the vehicle rather than just filling in the shape of a vehicle with the words if that makes sense! Thanks!
Running Shoe Glue
Newspaper Toilet Smell
Maud
Grandpa
Spreadsheets
Dario Flint
RJ Construction Shirts
Zori's
Something Special
Peanut Pip-Pops
Track & Field / Cross Country
Cleaning
Gardening / Yard Work
Hawaii
The Ridge @ Palani
Tapping Steering Wheel Driving
Small Pink Chair
Sunset Orange Vantor GT
Coral Bend Marlins
Big Thumbs
Big Toes
Tucking Shirt in Underwear
Everything Out!
ORVEN
Weatherman
Earthquake Cover
Wallets With Vertical CC Holders
Shave Ice
Mayo + Shoyu
Short Shorts
Smelly Feet
Blue Ice Chest
Aloha Shirts
Valcret 620's
Finger Jabbing Punishment
Thick Glasses
Otis / Sito
Driving Through Puddles
Hawaiian Juice
Racist Jokes
Instant Coffee
5 o'clock Shadow
5K/10K/ Marathons
Speedwork
Recycling Stash
Cajun Seasoning Aftermath
Sunday Barbeque
Bear Snore
Surfing
Ironing T-Shirts
Vacuum Carpet Lines
Willowmere Park
Backpack for Cash
Setting the Hook
Shoe Flexibility Test
Driving a Stickshift
Pistachio Almond
Dalbry's Shoes
Gold Chains
Speaker System
Rubbing our Legs
Laugh at Yourself
Love
Support
Advice
Selflessness
Sacrifice
Strength
Family
Local Pidgeon Accent

```html
<!DOCTYPE html>
<html lang="en">
<head>
<meta charset="utf-8">
<title>70 Years of Memories</title>
<link rel="stylesheet" href="https://fonts.googleapis.com/css2?family=Graduate&family=Oswald:wght@400;500;600&display=swap">
<style>
  :root {
    --paper: #ffffff;
    --ink-black: #1b1b1b;
    --ink-navy: #2d3a50;
    --ink-slate: #5f7372;
    --ink-sage: #7e9291;
    --ink-mist: #b7c3c1;
    --title-shadow: #7a7a7a;
  }
  html, body {
    margin: 0;
    padding: 0;
    width: 1200px;
    height: 800px;
    overflow: hidden;
    background: var(--paper);
  }
  .poster { display: block; width: 1200px; height: 800px; }
  .poster-title {
    font-family: "Graduate", serif;
    font-size: 158px;
    text-anchor: middle;
  }
  .title-shadow { fill: var(--title-shadow); stroke: var(--title-shadow); stroke-width: 44; stroke-linejoin: round; }
  .title-outline { fill: var(--ink-black); stroke: var(--paper); stroke-width: 22; stroke-linejoin: round; paint-order: stroke; }
  .title-face { fill: var(--ink-black); }
  .phrase { font-family: "Oswald", sans-serif; font-weight: 500; }
  .phrase-caps { font-family: "Oswald", sans-serif; font-weight: 600; text-transform: uppercase; }
  .ink-black { fill: var(--ink-black); }
  .ink-navy { fill: var(--ink-navy); }
  .ink-slate { fill: var(--ink-slate); }
  .ink-sage { fill: var(--ink-sage); }
  .ink-mist { fill: var(--ink-mist); }
</style>
</head>
<body>
<svg class="poster" viewBox="0 0 2340 1560" xmlns="http://www.w3.org/2000/svg" role="img" aria-label="70 Years of Memories: word art shaped like a station wagon">
  <defs>
    <path id="front-wheel-ring" d="M403,1020 A112,112 0 1 1 627,1020 A112,112 0 1 1 403,1020"/>
    <path id="rear-wheel-ring" d="M1810,1035 A115,115 0 1 1 2040,1035 A115,115 0 1 1 1810,1035"/>
    <path id="front-fender-arc" d="M369,916 A185,185 0 0 1 599,865"/>
    <path id="rear-fender-arc" d="M1725,1040 A190,190 0 0 1 2010,875"/>
    <path id="hood-curve" d="M608,858 Q700,920 712,1040"/>
  </defs>

  <!-- Heading -->
  <g class="poster-title">
    <text class="title-shadow" x="1182" y="257" textLength="1650" lengthAdjust="spacingAndGlyphs">70 YEARS OF MEMORIES</text>
    <text class="title-outline" x="1170" y="245" textLength="1650" lengthAdjust="spacingAndGlyphs">70 YEARS OF MEMORIES</text>
    <text class="title-face" x="1170" y="245" textLength="1650" lengthAdjust="spacingAndGlyphs">70 YEARS OF MEMORIES</text>
  </g>

  <!-- Roof line -->
  <g class="roof">
    <text class="phrase ink-navy" x="150" y="492" font-size="44" textLength="95" lengthAdjust="spacingAndGlyphs">Zori's</text>
    <text class="phrase ink-sage" x="263" y="488" font-size="44" textLength="305" lengthAdjust="spacingAndGlyphs">Something Special</text>
    <text class="phrase ink-slate" x="580" y="486" font-size="44" textLength="240" lengthAdjust="spacingAndGlyphs">Peanut Pip-Pops</text>
    <text class="phrase ink-navy" transform="translate(830 490) rotate(3)" font-size="46" textLength="485" lengthAdjust="spacingAndGlyphs">Track &amp; Field / Cross Country</text>
    <text class="phrase-caps ink-black" transform="translate(1318 530) rotate(41)" font-size="38" textLength="310" lengthAdjust="spacingAndGlyphs">Recycling Stash</text>
  </g>

  <!-- Pillars -->
  <g class="pillars">
    <text class="phrase ink-navy" transform="translate(118 692) rotate(-77)" font-size="30" textLength="190" lengthAdjust="spacingAndGlyphs">Sunday Barbeque</text>
    <text class="phrase ink-black" transform="translate(595 684) rotate(-70)" font-size="20" textLength="190" lengthAdjust="spacingAndGlyphs">Coral Bend Marlins</text>
    <text class="phrase-caps ink-black" transform="translate(625 682) rotate(-68)" font-size="30" textLength="190" lengthAdjust="spacingAndGlyphs">Blue Ice Chest</text>
    <text class="phrase-caps ink-black" transform="translate(1022 508) rotate(90)" font-size="26" textLength="188" lengthAdjust="spacingAndGlyphs">Hawaiian Juice</text>
    <text class="phrase ink-black" transform="translate(1062 508) rotate(84)" font-size="28" textLength="185" lengthAdjust="spacingAndGlyphs">Everything Out!</text>
    <text class="phrase ink-black" transform="translate(1408 712) rotate(-52)" font-size="38" textLength="82" lengthAdjust="spacingAndGlyphs">Maud</text>
  </g>

  <!-- Belt line -->
  <g class="belt-line">
    <text class="phrase ink-black" x="97" y="732" font-size="46" textLength="315" lengthAdjust="spacingAndGlyphs">Running Shoe Glue</text>
    <text class="phrase ink-sage" x="425" y="730" font-size="46" textLength="390" lengthAdjust="spacingAndGlyphs">Newspaper Toilet Smell</text>
    <text class="phrase ink-black" x="828" y="732" font-size="46" textLength="140" lengthAdjust="spacingAndGlyphs">Grandpa</text>
    <text class="phrase ink-mist" x="980" y="738" font-size="46" textLength="225" lengthAdjust="spacingAndGlyphs">Spreadsheets</text>
    <text class="phrase ink-navy" x="1217" y="745" font-size="46" textLength="195" lengthAdjust="spacingAndGlyphs">Dario Flint</text>
    <text class="phrase ink-sage" x="1420" y="755" font-size="46" textLength="100" lengthAdjust="spacingAndGlyphs">ORVEN</text>
    <text class="phrase-caps ink-navy" transform="translate(1568 742) rotate(5)" font-size="42" textLength="428" lengthAdjust="spacingAndGlyphs">RJ Construction Shirts</text>
    <text class="phrase-caps ink-sage" transform="translate(2008 778) rotate(7)" font-size="42" textLength="218" lengthAdjust="spacingAndGlyphs">Weatherman</text>
    <text class="phrase-caps ink-black" transform="translate(2242 796) rotate(80)" font-size="28" textLength="255" lengthAdjust="spacingAndGlyphs">5 O'Clock Shadow</text>
  </g>

  <!-- Front of car -->
  <g class="front-body">
    <text class="phrase ink-navy" transform="translate(98 876) rotate(-90)" font-size="24" textLength="135" lengthAdjust="spacingAndGlyphs">Valcret 620's</text>
    <text class="phrase ink-slate" x="145" y="780" font-size="40" textLength="445" lengthAdjust="spacingAndGlyphs">RJ Construction Shirts Family</text>
    <text class="phrase ink-mist" x="145" y="814" font-size="28" textLength="285" lengthAdjust="spacingAndGlyphs">Cajun Seasoning Aftermath</text>
    <text class="phrase ink-navy" x="145" y="850" font-size="28" textLength="215" lengthAdjust="spacingAndGlyphs">5K/10K/ Marathons</text>
    <text class="phrase ink-mist" x="130" y="882" font-size="22" textLength="212" lengthAdjust="spacingAndGlyphs">Driving Through Puddles</text>
    <text class="phrase-caps ink-navy" transform="translate(70 946) rotate(-90)" font-size="30" textLength="58" lengthAdjust="spacingAndGlyphs">Love</text>
    <text class="phrase ink-black" transform="translate(82 910) rotate(10)" font-size="32" textLength="84" lengthAdjust="spacingAndGlyphs">Advice</text>
    <text class="phrase ink-sage" x="172" y="937" font-size="40" textLength="170" lengthAdjust="spacingAndGlyphs">Otis / Sito</text>
    <text class="phrase-caps ink-navy" transform="translate(42 990) rotate(8)" font-size="48" textLength="305" lengthAdjust="spacingAndGlyphs">Instant Coffee</text>
    <text class="phrase-caps ink-mist" font-size="34"><textPath href="#front-fender-arc" textLength="250" lengthAdjust="spacingAndGlyphs">Small Pink Chair</textPath></text>
    <text class="phrase ink-navy" transform="translate(635 806) rotate(-90)" font-size="20" textLength="72" lengthAdjust="spacingAndGlyphs">Sacrifice</text>
    <text class="phrase ink-navy" transform="translate(640 812) rotate(57)" font-size="24" textLength="180" lengthAdjust="spacingAndGlyphs">Sunday Barbeque</text>
    <text class="phrase-caps ink-black" font-size="34"><textPath href="#hood-curve" textLength="215" lengthAdjust="spacingAndGlyphs">Mayo + Shoyu</textPath></text>
  </g>

  <!-- Front wheel -->
  <g class="wheel" transform="rotate(40 515 1020)">
    <text class="phrase-caps ink-black" font-size="44"><textPath href="#front-wheel-ring" textLength="680" lengthAdjust="spacingAndGlyphs">Shave Ice Smelly Feet Short Shorts</textPath></text>
  </g>

  <!-- Middle body -->
  <g class="middle-body">
    <text class="phrase ink-navy" x="755" y="785" font-size="38" textLength="298" lengthAdjust="spacingAndGlyphs">Local Pidgeon Accent</text>
    <text class="phrase ink-navy" x="688" y="826" font-size="32" textLength="180" lengthAdjust="spacingAndGlyphs">Dalbry's Shoes</text>
    <text class="phrase ink-sage" x="875" y="830" font-size="32" textLength="185" lengthAdjust="spacingAndGlyphs">Speaker System</text>
    <text class="phrase ink-mist" x="718" y="862" font-size="26" textLength="168" lengthAdjust="spacingAndGlyphs">Rubbing our Legs</text>
    <text class="phrase ink-navy" x="893" y="866" font-size="26" textLength="170" lengthAdjust="spacingAndGlyphs">Laugh at Yourself</text>
    <text class="phrase ink-navy" x="742" y="910" font-size="42" textLength="118" lengthAdjust="spacingAndGlyphs">Support</text>
    <text class="phrase ink-sage" x="872" y="912" font-size="42" textLength="182" lengthAdjust="spacingAndGlyphs">Selflessness</text>
    <text class="phrase ink-mist" x="746" y="948" font-size="26" textLength="306" lengthAdjust="spacingAndGlyphs">Tapping Steering Wheel Driving</text>
    <text class="phrase ink-navy" x="752" y="978" font-size="20" textLength="158" lengthAdjust="spacingAndGlyphs">Gardening / Yard Work</text>
    <text class="phrase ink-mist" x="915" y="980" font-size="20" textLength="135" lengthAdjust="spacingAndGlyphs">The Ridge @ Palani</text>
    <text class="phrase ink-black" transform="translate(1070 745) rotate(90)" font-size="42" textLength="240" lengthAdjust="spacingAndGlyphs">Blue Ice Chest</text>

    <text class="phrase ink-slate" x="1217" y="792" font-size="28" textLength="290" lengthAdjust="spacingAndGlyphs">Finger Jabbing Punishment</text>
    <text class="phrase ink-navy" x="1125" y="826" font-size="28" textLength="170" lengthAdjust="spacingAndGlyphs">Setting the Hook</text>
    <text class="phrase ink-slate" x="1302" y="830" font-size="28" textLength="202" lengthAdjust="spacingAndGlyphs">Shoe Flexibility Test</text>
    <text class="phrase ink-slate" x="1125" y="868" font-size="30" textLength="178" lengthAdjust="spacingAndGlyphs">Willowmere Park</text>
    <text class="phrase ink-mist" x="1310" y="872" font-size="30" textLength="202" lengthAdjust="spacingAndGlyphs">Backpack for Cash</text>
    <text class="phrase ink-mist" x="1125" y="910" font-size="32" textLength="125" lengthAdjust="spacingAndGlyphs">Bear Snore</text>
    <text class="phrase ink-navy" x="1260" y="914" font-size="32" textLength="242" lengthAdjust="spacingAndGlyphs">Vacuum Carpet Lines</text>
    <text class="phrase ink-mist" x="1120" y="950" font-size="28" textLength="266" lengthAdjust="spacingAndGlyphs">Tucking Shirt in Underwear</text>
    <text class="phrase ink-slate" x="1393" y="952" font-size="28" textLength="115" lengthAdjust="spacingAndGlyphs">Gold Chains</text>
    <text class="phrase ink-navy" x="1118" y="988" font-size="30" textLength="200" lengthAdjust="spacingAndGlyphs">Driving a Stickshift</text>
    <text class="phrase ink-mist" x="1328" y="992" font-size="30" textLength="180" lengthAdjust="spacingAndGlyphs">Pistachio Almond</text>

    <text class="phrase ink-navy" x="738" y="1040" font-size="44" textLength="535" lengthAdjust="spacingAndGlyphs">Wallets With Vertical CC Holders</text>
    <text class="phrase ink-navy" x="1283" y="1042" font-size="44" textLength="420" lengthAdjust="spacingAndGlyphs">Sunset Orange Vantor GT</text>
  </g>

  <!-- Rear body -->
  <g class="rear-body">
    <text class="phrase ink-black" transform="translate(1528 762) rotate(90)" font-size="46" textLength="225" lengthAdjust="spacingAndGlyphs">Aloha Shirts</text>
    <text class="phrase ink-mist" x="1585" y="805" font-size="42" textLength="165" lengthAdjust="spacingAndGlyphs">Big Thumbs</text>
    <text class="phrase ink-sage" x="1580" y="866" font-size="50" textLength="145" lengthAdjust="spacingAndGlyphs">Cleaning</text>
    <text class="phrase ink-mist" x="1580" y="928" font-size="48" textLength="110" lengthAdjust="spacingAndGlyphs">Hawaii</text>
    <text class="phrase ink-navy" x="1573" y="988" font-size="46" textLength="118" lengthAdjust="spacingAndGlyphs">Surfing</text>
    <text class="phrase ink-black" transform="translate(1755 902) rotate(-36)" font-size="28" textLength="170" lengthAdjust="spacingAndGlyphs">Ironing T-Shirts</text>
    <text class="phrase-caps ink-mist" font-size="34"><textPath href="#rear-fender-arc" textLength="390" lengthAdjust="spacingAndGlyphs">Finger Jabbing Punishment</textPath></text>
    <text class="phrase-caps ink-black" transform="translate(2022 850) rotate(55)" font-size="32" textLength="205" lengthAdjust="spacingAndGlyphs">Thick Glasses</text>
    <text class="phrase ink-mist" transform="translate(2068 822) rotate(45)" font-size="40" textLength="115" lengthAdjust="spacingAndGlyphs">Family</text>
    <text class="phrase ink-mist" transform="translate(2205 938) rotate(-76)" font-size="32" textLength="120" lengthAdjust="spacingAndGlyphs">Strength</text>
    <text class="phrase ink-slate" x="2145" y="968" font-size="26" textLength="125" lengthAdjust="spacingAndGlyphs">Racist Jokes</text>
    <text class="phrase-caps ink-black" x="2130" y="1048" font-size="32" textLength="142" lengthAdjust="spacingAndGlyphs">Speedwork</text>
  </g>

  <!-- Rear wheel -->
  <g class="wheel" transform="rotate(35 1925 1035)">
    <text class="phrase-caps ink-black" font-size="46"><textPath href="#rear-wheel-ring" textLength="700" lengthAdjust="spacingAndGlyphs">Surfing Earthquake Cover Big Toes</textPath></text>
  </g>
</svg>
</body>
</html>
```